**** Web design project for VornaSoft ****

For my ICT company VornaSoft I need a website.

We design, build and host web-applications and we have our own CMS product. In the references part we want to show sample websites (thumbnails) + links.

It should look modern (WEB 2.0), rounded corners.

I want the following menu' s:
- Home
- Services
- References
- News
- About VornaSoft
- Contact

Sample websites:
See attachments
http://www.plumvest.com
http://www.gadomirbureauwerk.nl

Reason: Want to take some time for feedback and improvements.

Reason: I'm waiting for a black background, with shadow and ambient light. You'll make a good chance!

Industry/Entity Type

It Company

Requirements
Must have
• - Fixed width (1024px), should fit on an IPad2
- Language selection English/Dutch
- Twitter/Facebook/LinkedIn/RSS icons
- Footer for Terms of use and Copyrights
- Search box
- 3 (or more) boxes for information i.e. news, blog or advertisements
Nice to have
• - Footer Site Map
- Contrasting background outside borders
- wide image (rotator) (with transperant sentence block)
- Shadow

```html
<!DOCTYPE html>
<html lang="en">
<head>
<meta charset="utf-8">
<title>VornaSoft – Web Hosting</title>
<link rel="stylesheet" href="https://fonts.googleapis.com/css2?family=Open+Sans:wght@300;400;600&family=Arimo:wght@400;700&display=swap">
<style>
:root{
  --page:#efefef;
  --white:#ffffff;
  --ink:#3a3a3a;
  --muted:#666666;
  --green:#5aa20c;
  --green-dark:#3f7d05;
  --green-light:#8fd02a;
  --link:#3d7d0c;
  --black:#151515;
  --line:#d9d9d9;
  --footer:#232323;
  --footer-text:#b9b9b9;
  --accent:#2a9fc9;
  --social-1:#3fa9e0;
  --social-2:#3b5998;
  --social-3:#1d87bd;
}
*{box-sizing:border-box;margin:0;padding:0}
html,body{width:728px;height:1200px;overflow:hidden}
body{background:var(--page);font-family:"Arimo",Arial,sans-serif;color:var(--ink);position:relative}
.abs{position:absolute}
a{color:var(--link)}

/* top bar */
.topbar{left:17px;top:13px;font-size:8.5px;color:var(--ink)}
.topbar a{margin:0 4px}
.topbar .sep{color:var(--muted)}
.search{left:601px;top:9px;width:111px;height:20px;background:var(--white);border:1px solid #d6d6d6;border-radius:5px;font-size:8.5px;color:#aaa;padding:5px 0 0 33px}
.search svg{position:absolute;right:6px;top:3px}

/* navigation */
.nav{left:15px;top:38px;width:697px;height:53px;border-radius:4px;background:linear-gradient(#3a3a3a,#0c0c0c);box-shadow:0 2px 4px rgba(0,0,0,.35)}
.brand{left:14px;top:13px;display:flex;align-items:center;gap:8px;font-family:"Open Sans",sans-serif;font-weight:400;font-size:18px;color:#a9c2cf}
.brand-dot{width:22px;height:22px;border-radius:50%;background:var(--accent)}
.menu{left:205px;top:0;height:53px;display:flex}
.menu li{list-style:none;height:53px;line-height:53px;text-align:center;font-family:"Open Sans",sans-serif;font-size:12px;color:var(--white);border-left:1px solid #333;letter-spacing:-.4px;white-space:nowrap}
.menu li:first-child{border-left:none;color:var(--green-light)}

/* hero */
.hero{left:15px;top:101px;width:697px;height:242px;border-radius:3px;overflow:hidden;background:radial-gradient(ellipse at 40% 55%,#a6e02e 0%,#6bb412 45%,#3f8a06 100%)}
.tabs{left:0;top:0;width:168px}
.tab{position:absolute;left:0;width:168px;height:60px;background:linear-gradient(#ffffff,#e4e4e4);border-bottom:1px solid #cfcfcf;padding:10px 0 0 28px}
.tab h3{font-family:"Open Sans",sans-serif;font-weight:300;font-size:20px;color:#333;letter-spacing:-.5px}
.tab p{font-size:8.5px;color:var(--green);margin-top:1px}
.tab.active{background:linear-gradient(#2c2c2c,#0e0e0e)}
.tab.active h3{color:var(--white)}
.tab.active p{color:var(--green-light)}
.tab-point{left:168px;top:0}
.hero-visual{left:195px;top:25px;width:320px;height:200px;border-radius:8px;background:radial-gradient(ellipse at 50% 50%,#2a2a2a 0%,#111 55%,rgba(17,17,17,0) 72%)}
.hero-copy{left:503px;top:52px;color:var(--white);font-family:"Open Sans",sans-serif}
.hero-copy .l1{font-size:19px;font-weight:300;letter-spacing:-.3px}
.hero-copy .l2{font-size:27px;font-weight:600;color:#222;letter-spacing:-1px;line-height:1;text-shadow:0 1px 0 rgba(255,255,255,.25)}
.hero-copy .l3{font-size:13px;margin-top:8px;letter-spacing:-.3px}
.hero-copy .l3 b{font-size:30px;font-weight:600;margin-left:6px;vertical-align:middle}

.btn{display:flex;align-items:center;justify-content:center;font-family:"Open Sans",sans-serif;font-size:11px;color:var(--white);border-radius:4px;letter-spacing:-.3px}
.btn-dark{background:linear-gradient(#3a3a3a,#0d0d0d);box-shadow:0 1px 2px rgba(0,0,0,.4)}
.btn-green{background:linear-gradient(#7cc625,#3f8a06);border:1px solid #3a7a07}
.hero-btn{left:576px;top:153px;width:93px;height:34px;font-size:12.5px}

/* band */
.band{left:0;top:390px;width:728px;height:590px;background:#f2f2f2}

/* service cards */
.card{top:354px;width:168px;height:242px;background:var(--white);border:1px solid #dcdcdc;border-radius:4px;box-shadow:0 1px 3px rgba(0,0,0,.1);overflow:hidden}
.card h2{height:40px;background:linear-gradient(#74bf1a,#4a9108);color:var(--white);font-family:"Open Sans",sans-serif;font-weight:300;font-size:17px;text-align:center;line-height:40px;letter-spacing:-.4px}
.card .thumb{position:absolute;left:9px;top:50px;width:150px;height:72px;border:1px solid #e2e2e2;box-shadow:0 2px 3px rgba(0,0,0,.12)}
.card p{position:absolute;left:18px;right:18px;top:140px;font-size:8.5px;line-height:14px;text-align:center;color:#444}
.card .btn{position:absolute;left:42px;top:196px;width:83px;height:27px}

/* news */
.h-section{font-family:"Open Sans",sans-serif;font-weight:300;font-size:21px;color:#444;letter-spacing:-.5px}
.news-item{left:38px;width:144px;height:79px;border-bottom:1px solid #e2e2e2}
.news-icon{position:absolute;left:0;top:2px;width:52px;height:52px;border-radius:6px}
.news-item p{position:absolute;left:61px;top:4px;font-size:8.5px;line-height:14px;color:#333}
.news-item a{position:absolute;left:61px;top:40px;font-size:8.5px;font-weight:700}

/* domain */
.domain-img{left:221px;top:657px;width:107px;height:69px;background:linear-gradient(#f4f4f4,#cfcfcf);border:1px solid #e3e3e3;box-shadow:0 2px 3px rgba(0,0,0,.12)}
.domain-input{left:353px;top:664px;width:155px;height:15px;background:var(--white);border:1px solid #ddd;border-radius:3px;font-size:8px;color:#999;padding:2px 8px}
.tld{font-size:8.5px;color:#333;display:flex;align-items:center;gap:3px}
.box{width:11px;height:11px;background:var(--white);border:1px solid #d2d2d2;border-radius:2px;display:inline-block}
.domain-btn{left:221px;top:739px;width:107px;height:23px}
.domain-links{left:353px;top:747px;font-size:8.5px;color:var(--muted)}
.domain-links a{margin:0 3px}
.about{left:221px;top:826px;width:466px;font-size:8.5px;line-height:14px;color:#444}
.about p{margin-bottom:8px}
.about-btn{left:221px;top:927px;width:73px;height:23px}

/* footer */
.footer{left:8px;top:985px;width:711px;height:149px;background:var(--footer)}
.fcol{top:0;height:149px;border-left:1px solid #3a3a3a}
.footer h4{position:absolute;top:30px;font-size:8.5px;color:var(--white);font-weight:700}
.flinks{position:absolute;top:45px;left:36px;list-style:none;font-size:8.5px;line-height:14px;color:var(--footer-text)}
.map{left:206px;top:47px;width:128px;height:84px;background:linear-gradient(135deg,#d9e2c8,#b9cde0);border:1px solid #555}
.nl-text{left:383px;top:48px;width:118px;font-size:8.5px;line-height:11px;color:var(--footer-text)}
.field{background:#e4e4e4;border-radius:3px;font-size:8px;color:#888;padding:2px 10px}
.fsubmit{font-family:"Arimo",sans-serif;font-size:7px;width:38px;height:11px;border-radius:3px}

/* bottom */
.copy{left:44px;top:1147px;font-size:8px;line-height:12px;color:#333}
.copy span{color:var(--green)}
.bottom-white{left:0;top:1134px;width:728px;height:66px;background:var(--white)}
.social{top:1147px;width:15px;height:15px;border-radius:3px}
</style>
</head>
<body>

<div class="abs bottom-white"></div>
<div class="abs band"></div>

<div class="abs topbar">24/7 Sales &amp; Support &nbsp; + 1 800 555 0142 <span class="sep">&nbsp;|</span><a href="#">Hot Deals</a><span class="sep">|</span><a href="#">Search</a></div>
<div class="abs search">Search
  <svg width="14" height="14" viewBox="0 0 14 14"><circle cx="6" cy="6" r="4.2" fill="none" stroke="#8a8a8a" stroke-width="1.6"/><line x1="9" y1="9" x2="13" y2="13" stroke="#8a8a8a" stroke-width="2"/></svg>
</div>

<header class="abs nav">
  <div class="abs brand"><span class="brand-dot"></span>VornaSoft</div>
  <ul class="abs menu">
    <li style="width:62px">HOME</li><li style="width:73px">SERVICES</li><li style="width:85px">HOSTING</li><li style="width:90px">REFERENCES</li><li style="width:82px">ABOUT US</li><li style="width:100px">CONTACTS</li>
  </ul>
</header>

<section class="abs hero">
  <div class="abs hero-visual" role="img" aria-label="Two black rack servers with green drive bays"></div>
  <div class="abs tabs">
    <div class="tab active" style="top:0"><h3>Web Hosting</h3><p>Get more information &nbsp;→</p></div>
    <div class="tab" style="top:61px"><h3>References</h3><p>Get more information &nbsp;→</p></div>
    <div class="tab" style="top:121px"><h3>News</h3><p>Get more information &nbsp;→</p></div>
    <div class="tab" style="top:182px;height:60px"><h3>Services</h3><p>Get more information &nbsp;→</p></div>
  </div>
  <svg class="abs tab-point" width="22" height="60" viewBox="0 0 22 60"><defs><linearGradient id="tp" x1="0" y1="0" x2="0" y2="1"><stop offset="0" stop-color="#2c2c2c"/><stop offset="1" stop-color="#0e0e0e"/></linearGradient></defs><polygon points="0,0 0,60 22,30" fill="url(#tp)"/></svg>
  <div class="abs hero-copy">
    <div class="l1">PROFESSIONAL</div>
    <div class="l2">WEB HOSTING</div>
    <div class="l3">Starts From: <b>$9.95</b></div>
  </div>
  <div class="abs btn btn-dark hero-btn">LEARN MORE</div>
</section>

<article class="abs card" style="left:15px"><h2>Web Designing</h2>
  <div class="thumb" role="img" aria-label="Blue globe illustration labelled web designing" style="background:linear-gradient(135deg,#d8ecf8,#2f7fc0)"></div>
  <p>Nam libero tempore, cum soluta nobis est eligendi optio cumque nihil impedit quo minus quod</p>
  <div class="btn btn-dark">LEARN MORE</div></article>
<article class="abs card" style="left:192px"><h2>Web Developing</h2>
  <div class="thumb" role="img" aria-label="Screenshot of a development timeline" style="background:linear-gradient(#f3f6f8,#dfe6ee)"></div>
  <p>Nam libero tempore, cum soluta nobis est eligendi optio cumque nihil impedit quo minus quod</p>
  <div class="btn btn-dark">LEARN MORE</div></article>
<article class="abs card" style="left:368px"><h2>Web Application</h2>
  <div class="thumb" role="img" aria-label="Screenshot of a blogging web application" style="background:linear-gradient(90deg,#fff 0%,#f0f0f0 55%,#8cd13a 100%)"></div>
  <p>Nam libero tempore, cum soluta nobis est eligendi optio cumque nihil impedit quo minus quod</p>
  <div class="btn btn-dark">LEARN MORE</div></article>
<article class="abs card" style="left:545px"><h2>CMS Products</h2>
  <div class="thumb" role="img" aria-label="Diagram of CMS platforms around a central hub" style="background:radial-gradient(circle,#3b8fd0 0%,#bcd9ef 35%,#ffffff 70%)"></div>
  <p>Nam libero tempore, cum soluta nobis est eligendi optio cumque nihil impedit quo minus quod</p>
  <div class="btn btn-dark">LEARN MORE</div></article>

<h2 class="abs h-section" style="left:42px;top:621px">News</h2>
<div class="abs news-item" style="top:663px"><div class="news-icon" role="img" aria-label="Disc and book icon" style="background:linear-gradient(135deg,#d8d8d8,#6a6a6a)"></div><p>Quickly and easily<br>create a Web Page</p><a href="#">Read More</a></div>
<div class="abs news-item" style="top:742px"><div class="news-icon" role="img" aria-label="Paper and pen icon" style="background:linear-gradient(135deg,#f4f4f4,#a8a8a8)"></div><p>Share documents<br>any time, any where</p><a href="#">Read More</a></div>
<div class="abs news-item" style="top:821px"><div class="news-icon" role="img" aria-label="Globe icon" style="background:radial-gradient(circle,#bdbdbd,#444)"></div><p>24/7 Real Person<br>Customer Support</p><a href="#">Read More</a></div>
<div class="abs news-item" style="top:900px;border-bottom:none"><div class="news-icon" role="img" aria-label="Floppy disk and CD icon" style="background:linear-gradient(135deg,#e0e0e0,#333)"></div><p>Online Account<br>Management Tools</p><a href="#">Read More</a></div>

<h2 class="abs h-section" style="left:219px;top:621px">Register Domain Name</h2>
<div class="abs domain-img" role="img" aria-label="Hand using a laptop"></div>
<div class="abs domain-input">enter domain name</div>
<div class="abs tld" style="left:354px;top:688px"><span class="box" style="position:relative"><svg width="11" height="11" viewBox="0 0 11 11" style="position:absolute;left:0;top:-1px"><polyline points="2,5.5 4.5,8 9,2.5" fill="none" stroke="#4b9a0a" stroke-width="1.6"/></svg></span>.mx</div>
<div class="abs tld" style="left:425px;top:688px"><span class="box"></span>.net</div>
<div class="abs tld" style="left:496px;top:688px"><span class="box"></span>.com</div>
<div class="abs tld" style="left:567px;top:688px"><span class="box"></span>.eu</div>
<div class="abs tld" style="left:638px;top:688px"><span class="box"></span>.us.com</div>
<div class="abs tld" style="left:354px;top:709px"><span class="box"></span>.us.com</div>
<div class="abs tld" style="left:425px;top:709px"><span class="box"></span>.info</div>
<div class="abs tld" style="left:496px;top:709px"><span class="box"></span>.mobi</div>
<div class="abs tld" style="left:567px;top:709px"><span class="box"></span>.co.uk</div>
<div class="abs tld" style="left:638px;top:709px"><span class="box"></span>.tv</div>
<div class="abs btn btn-green domain-btn">CHECK DOMAIN</div>
<div class="abs domain-links"><a href="#">Renew a domain</a>|<a href="#">Transfer a domain</a>|<a href="#">WHOIS</a></div>

<h2 class="abs h-section" style="left:219px;top:787px">About VornaSoft</h2>
<div class="abs about">
  <p>Nam libero tempore, cum soluta nobis est eligendi optio cumque nihil impedit quo minus quod maxime placeat facere possimus, omnis voluptas assumenda est, omnis dolor repellendus. Temporibus autem quibusdam et aut officiis debitis aut rerum necessitatibus saepe eveniet.</p>
  <p>Voluptates repudiandae sint et molestiae non recusandae. Itaque earum rerum hic tenetur a sapiente delectus, ut aut reiciendis voluptatibus maiores alias consequatur aut perferendis doloribus asperiores repellat. Lorem ipsum dolor sit amet, consectetur adipisicing elit, sed do eiusmod tempor incididunt ut labore et dolore.</p>
</div>
<div class="abs btn btn-green about-btn">READ MORE</div>

<footer class="abs footer">
  <h4 style="left:36px">About</h4>
  <ul class="flinks"><li>Careers</li><li>Security Center</li><li>Company Info</li><li>News Center</li><li>Customer Testimonials</li><li>What's New</li></ul>
  <div class="abs fcol" style="left:177px"></div>
  <h4 style="left:206px">Site Map</h4>
  <div class="abs map" role="img" aria-label="Map of South Asia"></div>
  <div class="abs fcol" style="left:355px"></div>
  <h4 style="left:383px">News Letter</h4>
  <div class="abs nl-text">Lorem Ipsum is simply dummy text of the printing and typesetting industry Lorem Ipsum has been the indus-</div>
  <div class="abs field" style="left:383px;top:98px;width:103px;height:13px">Enter Your E-mail ID</div>
  <div class="abs btn btn-green fsubmit" style="left:448px;top:121px">Submit</div>
  <div class="abs fcol" style="left:532px"></div>
  <h4 style="left:556px">Quick Contact</h4>
  <div class="abs field" style="left:556px;top:47px;width:103px;height:13px">Name</div>
  <div class="abs field" style="left:556px;top:66px;width:103px;height:13px">E-mail</div>
  <div class="abs field" style="left:556px;top:85px;width:103px;height:27px;padding-top:6px">Comment</div>
  <div class="abs btn btn-green fsubmit" style="left:621px;top:121px">Submit</div>
</footer>

<div class="abs copy"><span>@Copyrights</span> All right reserved<br>provided bya</div>
<div class="abs social" style="left:609px;background:var(--social-1)" aria-label="Social link one"></div>
<div class="abs social" style="left:631px;background:var(--social-2)" aria-label="Social link two"></div>
<div class="abs social" style="left:653px;background:var(--social-3)" aria-label="Social link three"></div>

</body>
</html>
```